Business Card Design Project

I need a 2 sided business card - 1 side to promote my business "Plan TRQD" - and the other side to promote my fundraising initiative "OnTheSpinSnaps".

Please find attached photo referred to in my feedback email

Target Market(s)

Plan TRQD - financial professionals; OnTheSpinSnaps - anyone

Industry/Entity Type

Business

Requirements
Must have
• Must complement existing design work.

1. For Plan TRQD: Include orange block (with text Plan TRQD)
refer to www.plantrqd.com.au and/or
https://www.facebook.com/PlanTRQD or other social media

2. must include in no particular order - Name: Joanna Pritchett; Title: Managing Director; Website: www.plantrqd.com.au; Email: joanna@plantrqd.com.au; Ph: 1300 462 951; website: http://aboutpage.example/joannapritchett; social media icons as per website ie FB, twitter, Google+, LinkedIn, YouTube, Pinterest

For OnTheSpinSnaps: https://www.facebook.com/OnTheSpinSnaps or other social media

1. must include in no particular order - Name: Joanna Pritchett; Title: Founder; email: joanna@plantrqd.com.au; website: http://aboutpage.example/joannapritchett; social media icons as per website ie FB, twitter, Google+, LinkedIn, Pinterest
Nice to have
• For Plan TRQD: include dark block with tagline (eLearning, Competency, Performance) - either vertically or horizontally to orange block

For OnTheSpinSnaps: include tagline - Simply Fundraising

```html
<!DOCTYPE html>
<html lang="en">
<head>
<meta charset="utf-8">
<title>Plan TRQD / OnTheSpinSnaps business card</title>
<link rel="stylesheet" href="https://fonts.googleapis.com/css2?family=Open+Sans:wght@400;700;800&family=Roboto+Condensed:wght@300;400&family=Roboto:wght@400&display=swap">
<style>
  :root {
    --page: #ffffff;
    --ink: #1c1c1c;
    --orange: #f9ad1a;
    --charcoal: #1f1c1b;
    --slate: #333e42;
    --tagline-grey: #9d9d9d;
    --lime: #c3d55b;
    --icon-grey: #7b7b7b;
    --lettering-tone: #e4e4e4;
    --border: #2a2a2a;
  }
  * { box-sizing: border-box; margin: 0; padding: 0; }
  html, body {
    width: 985px; height: 1200px; overflow: hidden;
    background: var(--page);
  }
  .sheet { position: relative; width: 985px; height: 1200px; }

  .side-label {
    position: absolute; left: 0; width: 985px; text-align: center;
    font-family: "Roboto", Arial, sans-serif; font-weight: 400;
    font-size: 54px; line-height: 64px; color: var(--ink);
  }
  .side-label--front { top: 158px; }
  .side-label--back { top: 1003px; }

  .card {
    position: absolute; left: 203px; width: 587px; height: 335px;
    border: 1px solid var(--border); overflow: hidden;
  }
  .card--front { top: 250px; background: var(--charcoal); }
  .card--back { top: 645px; background: var(--page); }

  /* front */
  .brand-block {
    position: absolute; left: 0; top: 0; width: 296px; height: 100%;
    background: var(--orange); border-right: 3px solid var(--page);
  }
  .brand-name {
    position: absolute; left: 38px; top: 110px;
    font-family: "Open Sans", Arial, sans-serif; font-weight: 800;
    font-size: 44px; line-height: 1; color: var(--slate); letter-spacing: -1px;
  }
  .contact {
    position: absolute; left: 30px;
    font-family: "Roboto Condensed", Arial, sans-serif; font-weight: 400;
    font-size: 15.5px; line-height: 20px; color: var(--ink);
    list-style: none;
  }
  .card--front .contact { top: 257px; }
  .identity {
    position: absolute; left: 411px; top: 18px;
    font-family: "Open Sans", Arial, sans-serif; font-size: 17.5px;
    line-height: 25px; color: #f2f2f2;
  }
  .tagline {
    position: absolute; left: 337px; top: 128px; list-style: none;
    font-family: "Open Sans", Arial, sans-serif; font-size: 24px;
    line-height: 34px; color: var(--tagline-grey);
  }
  .social-strip {
    position: absolute; left: 299px; top: 277px; width: 288px; height: 45px;
    background: var(--page);
  }
  .social-strip svg { position: absolute; left: 38px; top: 10px; }

  /* back */
  .top-band { position: absolute; left: 0; top: 0; width: 100%; height: 6px; background: var(--lime); }
  .bottom-band { position: absolute; left: 0; top: 253px; width: 100%; height: 82px; background: var(--lime); }
  .project-block {
    position: absolute; left: 13px; top: 27px; width: 227px; height: 228px;
    background: var(--lime);
  }
  .project-name {
    position: absolute; left: 0; top: 96px; width: 227px; text-align: center;
    font-family: "Open Sans", Arial, sans-serif; font-weight: 800;
    font-size: 21px; color: var(--page); letter-spacing: -0.5px;
  }
  .card--back .identity {
    left: 451px; top: 18px; color: var(--ink);
    font-family: "Roboto Condensed", Arial, sans-serif; font-size: 17.5px; line-height: 22px;
  }
  .lettered-tagline {
    position: absolute; left: 265px; top: 146px; width: 295px; height: 46px;
    background: linear-gradient(90deg, var(--lettering-tone), #f1f1f1);
    border-radius: 4px;
  }
  .card--back .contact { top: 269px; }
</style>
</head>
<body>
<main class="sheet">
  <h2 class="side-label side-label--front">Front</h2>

  <section class="card card--front" aria-label="Plan TRQD card front">
    <div class="brand-block">
      <p class="brand-name">Plan TRQD</p>
      <ul class="contact">
        <li>Ph: 1300 462 951</li>
        <li>Email: joanna@plantrqd.com.au</li>
        <li>Website: www.plantrqd.com.au</li>
      </ul>
    </div>
    <p class="identity">Joanna Pritchett<br>Managing Director</p>
    <ul class="tagline">
      <li>eLearning</li>
      <li>Competency</li>
      <li>Performance</li>
    </ul>
    <div class="social-strip">
      <svg width="224" height="28" viewBox="0 0 224 28" role="img" aria-label="Social media links">
        <g fill="var(--icon-grey)">
          <rect x="0" y="0" width="28" height="28" rx="4"/>
          <rect x="32" y="0" width="28" height="28" rx="4"/>
          <rect x="64" y="0" width="28" height="28" rx="4"/>
          <rect x="96" y="0" width="28" height="28" rx="4"/>
          <rect x="128" y="0" width="28" height="28" rx="4"/>
          <rect x="163" y="0" width="28" height="28" rx="4"/>
          <rect x="196" y="0" width="28" height="28" rx="4"/>
        </g>
      </svg>
    </div>
  </section>

  <section class="card card--back" aria-label="OnTheSpinSnaps card back">
    <div class="top-band"></div>
    <div class="project-block">
      <p class="project-name">OnTheSpinSnaps</p>
    </div>
    <p class="identity">Joanna Pritchett<br>Founder</p>
    <div class="lettered-tagline" role="img" aria-label="Hand-lettered fundraising tagline"></div>
    <div class="bottom-band"></div>
    <ul class="contact">
      <li>Ph: 1300 462 951</li>
      <li>Email: joanna@plantrqd.com.au</li>
      <li>Website: www.plantrqd.com.au</li>
    </ul>
  </section>

  <h2 class="side-label side-label--back">Back</h2>
</main>
</body>
</html>
```